Mend Your Frame
Stationary
Project: Mend Your Frame
Mend Your Frame - Health
Creative Brief
Use specific fonts
Whatever fonts look best!
Professional
Dellan Corvin
Body Composition Specialist/ Personal Trainer
Dont put address.
dellcorvin@mailnest.example
MendYourFrameAnalysis.example
We use a state of the art body composition analyzer to accurately determine total body fat, essential fat, non essential fat, reserve fat, total body water, and lean mass. It's fast, non-invasive, and comparable to the Gold Standard. To find out more visit our website or call us.

```html
<!DOCTYPE html>
<html lang="en">
<head>
<meta charset="utf-8">
<title>Mend Your Frame — Business Card</title>
<link rel="stylesheet" href="https://fonts.googleapis.com/css2?family=Open+Sans:ital,wght@0,400;0,600;0,700;0,800;1,700&display=swap">
<style>
  :root {
    --backdrop: #3a3a3c;
    --card-white: #ffffff;
    --blue-light: #2f9be0;
    --blue-mid: #1c6fc4;
    --blue-deep: #164f9e;
    --edge-grey: #8e9096;
    --brand-blue: #1d6cc0;
    --text-white: #ffffff;
  }
  * { margin: 0; padding: 0; box-sizing: border-box; }
  html, body {
    width: 1200px; height: 780px; overflow: hidden;
    background: var(--backdrop);
    font-family: "Open Sans", Arial, sans-serif;
  }
  .business-card {
    position: absolute; left: 100px; top: 104px;
    width: 1000px; height: 572px;
    border-radius: 26px; overflow: hidden;
  }
  .card-shapes { position: absolute; inset: 0; }
  .brand-lockup {
    position: absolute; left: 34px; top: 250px;
    display: flex; align-items: flex-start; gap: 16px;
  }
  .brand-mark {
    width: 22px; height: 22px; margin-top: 24px;
    background: var(--brand-blue); flex: none;
  }
  .brand-name {
    font-weight: 800; font-size: 34px; line-height: 1.02;
    color: var(--brand-blue); letter-spacing: -0.5px;
    text-transform: uppercase;
  }
  .brand-tagline {
    margin-top: 14px;
    font-weight: 600; font-size: 13px; line-height: 1.3;
    color: var(--brand-blue);
  }
  .holder {
    position: absolute; right: 44px; top: 40px; text-align: right;
    color: var(--text-white);
  }
  .holder-name { font-weight: 700; font-size: 38px; line-height: 1.15; }
  .holder-role { font-weight: 700; font-style: italic; font-size: 19px; line-height: 1.35; }
  .contact-list {
    position: absolute; right: 40px; bottom: 46px;
    list-style: none; color: var(--text-white); text-align: right;
  }
  .contact-item {
    display: flex; justify-content: flex-end; align-items: center;
    gap: 16px; font-size: 22px; line-height: 1.75;
  }
  .contact-icon { width: 22px; height: 22px; flex: none; }
</style>
</head>
<body>
  <article class="business-card">
    <svg class="card-shapes" viewBox="0 0 1000 572" width="1000" height="572" aria-hidden="true">
      <defs>
        <radialGradient id="blueField" cx="72%" cy="42%" r="70%">
          <stop offset="0" stop-color="var(--blue-light)"/>
          <stop offset="0.6" stop-color="var(--blue-mid)"/>
          <stop offset="1" stop-color="var(--blue-deep)"/>
        </radialGradient>
      </defs>
      <rect width="1000" height="572" fill="url(#blueField)"/>
      <path d="M0 0 H320 C420 150 420 420 300 572 H0 Z" fill="var(--edge-grey)"/>
      <path d="M0 0 H300 C400 150 400 420 280 572 H0 Z" fill="var(--card-white)"/>
    </svg>

    <div class="brand-lockup">
      <span class="brand-mark"></span>
      <div class="brand-text">
        <div class="brand-name">Mend Your<br>Frame</div>
        <p class="brand-tagline">Move well.<br>Rest easy.<br>Live strong daily.</p>
      </div>
    </div>

    <header class="holder">
      <h1 class="holder-name">Dellan Corvin</h1>
      <p class="holder-role">Body Composition Specialist</p>
      <p class="holder-role">Personal Trainer</p>
    </header>

    <ul class="contact-list">
      <li class="contact-item">555.014.2290
        <svg class="contact-icon" viewBox="0 0 24 24"><path d="M6 3l4 4-2 3c1 2 4 5 6 6l3-2 4 4-3 3C10 21 3 14 3 6z" fill="#fff"/></svg>
      </li>
      <li class="contact-item">dellcorvin@mailnest.example
        <svg class="contact-icon" viewBox="0 0 24 24"><circle cx="12" cy="12" r="4" fill="none" stroke="#fff" stroke-width="2.4"/><path d="M16 8v6c0 2 4 2 4-2a8 8 0 1 0-3 6" fill="none" stroke="#fff" stroke-width="2.4"/></svg>
      </li>
      <li class="contact-item">www.MendYourFrameAnalysis.example
        <svg class="contact-icon" viewBox="0 0 24 24"><g fill="none" stroke="#fff" stroke-width="2"><circle cx="12" cy="12" r="9"/><ellipse cx="12" cy="12" rx="4" ry="9"/><path d="M3 12h18M5 7h14M5 17h14"/></g></svg>
      </li>
    </ul>
  </article>
</body>
</html>
```